Half wrap for electrical company

No too busy. Simple. Our target audience is semi/full retired with disposal income that wants things completed right the 1st time and looking for our van to say the same thing. I was drawn to your website because I found Design 23141373 to be impressive. I like how the dots give the whole design depth.

Van Make and Model:
https://www.qorvel.com/vans/kelpra/passenger
https://www.qorvel.com/content/dam/qorvel/na/us/english/index/vehicles/2023/vans/kelpra-passenger/01-images/2022-kelpra-passenger-details-2500-specs-highlights-v2.jpg?imwidth=960

Target Market(s)

55+ living in a 2nd home

Industry/Entity Type

Electrical

Requirements
Must have
• My logo, my business phone number (729)316-4058
Should not have
• Don't need anything on the hood.

```html
<!DOCTYPE html>
<html lang="en">
<head>
<meta charset="utf-8">
<title>Halvern Electric – Van Wrap</title>
<link href="https://fonts.googleapis.com/css2?family=Montserrat:wght@600;700&family=Yellowtail&display=swap" rel="stylesheet">
<style>
  :root {
    --backdrop: #7b7b7b;
    --wrap-black: #121314;
    --wrap-white: #f4f4f4;
    --wrap-orange: #e8702a;
    --band-orange: #e8823f;
    --glass: #3a3d40;
    --tyre: #2a2a2a;
    --rim: #bfc2c5;
    --text-dark: #111111;
    --text-light: #ffffff;
  }
  html, body {
    margin: 0;
    padding: 0;
    width: 1200px;
    height: 575px;
    overflow: hidden;
    background: var(--backdrop);
  }
  .wrap-canvas { display: block; width: 1200px; height: 575px; }
  .body-black { fill: var(--wrap-black); }
  .panel-white { fill: var(--wrap-white); }
  .band-orange { fill: var(--band-orange); }
  .lower-orange { fill: var(--wrap-orange); }
  .stripe-white { fill: var(--wrap-white); }
  .side-window { fill: var(--glass); }
  .tyre { fill: var(--tyre); }
  .rim { fill: var(--rim); }
  .logo-disc { fill: var(--wrap-white); }
  .brand-name, .brand-sub {
    font-family: "Montserrat", sans-serif;
    font-weight: 700;
    fill: var(--text-dark);
  }
  .brand-name { font-size: 66px; letter-spacing: 1px; }
  .brand-sub { font-size: 28px; letter-spacing: 12px; }
  .web-address {
    font-family: "Montserrat", sans-serif;
    font-weight: 700;
    font-size: 30px;
    fill: var(--text-light);
  }
  .call-label {
    font-family: "Yellowtail", cursive;
    font-size: 32px;
    fill: var(--text-light);
  }
  .phone-number {
    font-family: "Montserrat", sans-serif;
    font-weight: 700;
    font-size: 30px;
    letter-spacing: 1px;
    fill: var(--text-light);
  }
</style>
</head>
<body>
<svg class="wrap-canvas" viewBox="0 0 1200 575" xmlns="http://www.w3.org/2000/svg" aria-label="Halvern Electric half wrap, side view">
  <defs>
    <clipPath id="van-shape">
      <path d="M55,300 Q62,250 130,242 L240,236 L352,114 Q362,105 384,105 L1072,98 Q1098,100 1106,132 L1128,300 L1138,400 L1150,418 L1150,432 L60,442 Q50,420 52,380 Z"/>
    </clipPath>
  </defs>

  <g class="van" clip-path="url(#van-shape)">
    <rect class="body-black" x="0" y="0" width="1200" height="575"/>
    <polygon class="panel-white" points="560,100 1200,90 1200,230 700,274 560,290"/>
    <polygon class="band-orange" points="700,274 1200,230 1200,268 700,312"/>
    <polygon class="stripe-white" points="700,314 1200,270 1200,275 700,319"/>
    <polygon class="stripe-white" points="270,346 700,304 700,311 270,352"/>
    <polygon class="lower-orange" points="275,356 700,316 700,445 290,445"/>
    <path class="side-window" d="M330,238 L395,128 L484,124 L484,236 Z"/>
  </g>

  <g class="wheel">
    <circle class="tyre" cx="222" cy="455" r="72"/>
    <circle class="rim" cx="222" cy="455" r="48"/>
  </g>
  <g class="wheel">
    <circle class="tyre" cx="925" cy="455" r="72"/>
    <circle class="rim" cx="925" cy="455" r="48"/>
  </g>

  <circle class="logo-disc" cx="612" cy="250" r="110"/>
  <g class="brand" transform="rotate(-4.5 736 205)">
    <text class="brand-name" x="736" y="205">HALVERN</text>
    <text class="brand-sub" x="806" y="240">ELECTRIC</text>
  </g>

  <text class="web-address" x="762" y="298" transform="rotate(-5 762 298)">HalvernElectric.com</text>

  <g class="phone-line" transform="rotate(-6 193 307)">
    <text class="call-label" x="193" y="307">Call</text>
    <text class="phone-number" x="250" y="303">(729)316-4058</text>
  </g>
</svg>
</body>
</html>
```